Awesome Pavement Maintenance Company Needs New Postcard!

We are an Asphalt Maintenance contractor in need of a new Postcard design for our Fall direct mail campaign. Our services include Crack Filling, Sealcoating, Line Striping and Asphalt Patching. Fall is a busy time of year for Parking Lot Maintenance services in Connecticut, USA where we are located, and we need to capture as much business from this mail piece as we possibly can. People enlist our services in preparation for winter so the winning design will have a call to action that we think has the best chance of getting our phone to ring. Come up with a new look and feel for us in your design.

Feel free to use our images attached, or stock images. An example of one of our current cards is attached also. PLEASE: use the template provided for layout specifications.

Target Market(s)

Commercial/Industrial Facility Managers, Condo/Apartment Building Property Managers, Owners of Commercial Real Estate, Business Owners, etc.

Industry/Entity Type

Construction Company

Requirements
Must have
• A Call to Action
• Our Phone Number: 860-417-2938
• Our website: www.brinweldpavement.example
Nice to have
• Our 4 Main Services Listed
• -Asphalt Patching
• - Crack Filling
• -Sealcoating
• -Line Striping
• Photos? We have plenty or use stock
Should not have
• Misspelling of our name. Should be BrinWELD -not 'coast'!

```html
<!DOCTYPE html>
<html lang="en">
<head>
<meta charset="utf-8">
<title>BrinWELD Pavement Services – Fall Postcard</title>
<link href="https://fonts.googleapis.com/css2?family=Oswald:wght@400;500;600&family=Roboto+Condensed:wght@400;700&family=Open+Sans:wght@400;700&display=swap" rel="stylesheet">
<style>
  :root {
    --brand-red: #a8323a;
    --ink: #111111;
    --paper: #ffffff;
    --band-black: #0d0d0d;
    --asphalt: #3a3f4a;
    --grass: #6f7d4a;
  }
  * { box-sizing: border-box; margin: 0; padding: 0; }
  html, body { width: 1200px; height: 389px; overflow: hidden; background: var(--paper); }
  .postcard { position: relative; width: 1200px; height: 389px; background: var(--paper); }

  /* Mailing side */
  .mail-side { position: absolute; left: 0; top: 0; width: 600px; height: 389px; }
  .brand-mark { position: absolute; left: 10px; top: 12px; display: flex; align-items: flex-start; gap: 8px; }
  .brand-name-small { font-family: "Open Sans", sans-serif; font-weight: 700; font-size: 20px; line-height: 20px; color: var(--brand-red); }
  .brand-tag-small { font-family: "Open Sans", sans-serif; font-weight: 700; font-size: 7.5px; letter-spacing: .3px; color: var(--ink); margin-top: 3px; }
  .return-address { font-family: "Open Sans", sans-serif; font-size: 7.5px; line-height: 10.5px; color: var(--ink); margin-top: 0; }
  .return-address .web { color: var(--brand-red); font-weight: 700; }
  .headline { position: absolute; left: 28px; top: 52px; font-family: "Oswald", sans-serif; font-weight: 600; font-size: 38px; line-height: 39px; color: var(--ink); text-transform: uppercase; letter-spacing: -.2px; }
  .call-line { position: absolute; left: 28px; top: 180px; font-family: "Roboto Condensed", sans-serif; font-size: 21px; color: var(--brand-red); }
  .call-line .phone { color: var(--ink); }
  .call-follow { position: absolute; left: 101px; top: 206px; font-family: "Roboto Condensed", sans-serif; font-size: 21px; color: var(--brand-red); }
  .crew-photo { position: absolute; left: 0; top: 212px; width: 91px; height: 177px; background: linear-gradient(180deg, #c9ced6 0%, #9aa3ad 35%, #4b5059 100%); }
  .service-list { position: absolute; left: 106px; top: 232px; list-style: none; font-family: "Roboto Condensed", sans-serif; font-size: 16px; line-height: 22px; color: var(--ink); }
  .service-list li::before { content: "•"; color: var(--brand-red); margin-right: 4px; }

  /* Image side */
  .promo-side { position: absolute; left: 600px; top: 0; width: 600px; height: 389px; }
  .promo-banner { height: 92px; background: var(--brand-red); display: flex; align-items: center; justify-content: center; }
  .promo-title { font-family: "Oswald", sans-serif; font-weight: 500; font-size: 66px; line-height: 1; color: var(--paper); letter-spacing: 1px; }
  .lot-photo { height: 210px; background: linear-gradient(160deg, var(--grass) 0%, #5c6a45 18%, var(--asphalt) 30%, #2f343e 75%, #56604a 100%); }
  .promo-footer { display: flex; height: 87px; }
  .cta-band { width: 406px; background: var(--band-black); padding: 12px 0 0 22px; font-family: "Oswald", sans-serif; color: var(--paper); }
  .cta-main { font-size: 33px; line-height: 38px; font-weight: 400; }
  .cta-main .phone { color: var(--brand-red); }
  .cta-sub { font-size: 17px; line-height: 24px; margin-top: 4px; }
  .cta-sub small { font-size: 8px; color: var(--brand-red); vertical-align: middle; }
  .brand-box { flex: 1; background: var(--paper); display: flex; flex-direction: column; align-items: center; justify-content: center; font-family: "Open Sans", sans-serif; }
  .brand-name-large { font-weight: 700; font-size: 30px; line-height: 32px; color: var(--brand-red); }
  .brand-tag-large { font-weight: 700; font-size: 12px; letter-spacing: .6px; color: var(--ink); margin-top: 3px; }
  .brand-web { font-size: 10.5px; color: var(--brand-red); margin-top: 2px; }
</style>
</head>
<body>
<div class="postcard">
  <section class="mail-side">
    <div class="brand-mark">
      <div>
        <div class="brand-name-small">BrinWELD</div>
        <div class="brand-tag-small">PAVEMENT SERVICES</div>
      </div>
      <div class="return-address">
        P.O. Box 382<br>
        Millbrook, CT 06412<br>
        <span class="web">brinweldpavement.example</span>
      </div>
    </div>
    <h1 class="headline">Soon it’ll be cold<br>and the asphalt cracks<br>will be forming.</h1>
    <p class="call-line">Call us now at <span class="phone">860-417-2938</span></p>
    <p class="call-follow">and we’ll take care of it. Pronto!</p>
    <div class="crew-photo" role="img" aria-label="Crew member pushing a line striping machine across a parking lot"></div>
    <ul class="service-list">
      <li>Asphalt Patching</li>
      <li>Crack Filling</li>
      <li>Sealcoating</li>
      <li>Line Striping</li>
    </ul>
  </section>

  <section class="promo-side">
    <div class="promo-banner"><h2 class="promo-title">BEAUTIFUL, RIGHT?</h2></div>
    <div class="lot-photo" role="img" aria-label="Aerial view of a freshly sealcoated and striped parking lot surrounded by grass"></div>
    <div class="promo-footer">
      <div class="cta-band">
        <div class="cta-main">CALL <span class="phone">860-417-2938</span> TODAY</div>
        <div class="cta-sub">TO LEARN HOW WE CAN DO THAT FOR YOU. <small>(BECAUSE WE CAN.)</small></div>
      </div>
      <div class="brand-box">
        <div class="brand-name-large">BrinWELD</div>
        <div class="brand-tag-large">PAVEMENT SERVICES</div>
        <div class="brand-web">www.brinweldpavement.example</div>
      </div>
    </div>
  </section>
</div>
</body>
</html>
```